A new company focused on starting and investing in transformative businesses.

We need a simple and clean website with a few pages. we like marlowvest.com as a starting point. we want the landing page to be very simple with an option to click through on the top right into INVESTOR LOGIN. then we want to be able to scroll down to see more about our company.

Target Market(s)

professional

Coding

Coded - Design and coding required

Number of Pages Required

2 page

Font styles to use
Serif
Sans Serif

Requirements
Must have
• HALVERN BUILDERS logo (attached as a file) on the top with INVESTOR LOGIN as a click through on the right. Please model the click through from marlowvest.com. The description (also written in attached file) should be on the landing page. we do not want to have to scroll to read the description.

Then we can scroll down to read more about Halvern including the mission and the two types of businesses. More is detailed on the attached file called "Halvern Website Syntax"
Should not have
• should not be slow loading with lots of fancy graphics. should not be busy and with too many colors.

```html
<!DOCTYPE html>
<html lang="en">
<head>
<meta charset="utf-8">
<title>Halvern Builders</title>
<link rel="stylesheet" href="https://fonts.googleapis.com/css2?family=Montserrat:wght@400;500;600;700&family=Oswald:wght@600;700&display=swap">
<style>
  :root {
    --brand: #0a57a0;
    --brand-dark: #084a8a;
    --tint: #eaf2fc;
    --ink: #111418;
    --body: #222a33;
    --white: #ffffff;
  }
  * { box-sizing: border-box; margin: 0; padding: 0; }
  html, body { width: 1200px; height: 2602px; overflow: hidden; background: var(--white); }
  body { position: relative; font-family: "Montserrat", Arial, sans-serif; color: var(--body); }
  .abs { position: absolute; }
  .btn {
    position: absolute; display: flex; align-items: center; justify-content: center;
    background: var(--brand); color: var(--white); font-weight: 600; font-size: 13.5px;
    letter-spacing: .6px; text-transform: uppercase; text-decoration: none;
  }

  /* header */
  .brand { left: 150px; top: 12px; height: 66px; display: flex; align-items: center; gap: 12px; }
  .brand-square { width: 52px; height: 66px; background: var(--brand); }
  .brand-name { font-size: 23px; font-weight: 500; color: var(--brand); line-height: 27px; letter-spacing: .5px; }
  .login { left: 891px; top: 24px; width: 158px; height: 42px; }

  /* hero */
  .hero-band { left: 0; top: 90px; width: 1200px; height: 534px; background: var(--tint); }
  .hero-photo { left: 673px; top: 158px; width: 527px; height: 517px; background: linear-gradient(160deg, #4d8fd6 0%, #6ea7e4 35%, #2a3f58 75%, #1a2430 100%); }
  .hero-title { left: 150px; top: 234px; font-family: "Oswald", Impact, sans-serif; font-weight: 700; font-size: 52px; line-height: 68px; color: var(--brand); letter-spacing: .5px; }
  .hero-text { left: 152px; top: 309px; width: 460px; font-size: 21px; line-height: 30px; color: var(--ink); white-space: nowrap; }
  .contact { left: 150px; top: 416px; width: 180px; height: 48px; }

  /* mission */
  .mission-title { left: 0; width: 1200px; top: 748px; text-align: center; font-size: 34px; font-weight: 700; color: var(--brand); letter-spacing: .5px; }
  .mission-photo { left: 0; top: 823px; width: 564px; height: 397px; background: linear-gradient(120deg, #e4e6e8 0%, #cfd4d8 45%, #2c4f5e 70%, #1b2838 100%); }
  .mission-text { left: 632px; top: 846px; font-size: 31px; line-height: 45px; color: var(--ink); white-space: nowrap; }
  .mission-text b { font-weight: 700; }

  /* ventures */
  .venture-tab { left: 587px; top: 1175px; width: 143px; height: 70px; background: var(--tint); }
  .venture-band { left: 0; top: 1243px; width: 730px; height: 465px; background: var(--tint); }
  .venture-photo { left: 653px; top: 1255px; width: 396px; height: 270px; background: linear-gradient(135deg, #3b3229 0%, #8a7a68 40%, #d9d2c6 65%, #4a3f35 100%); }
  .venture { left: 152px; width: 470px; }
  .venture h3 { font-size: 19px; font-weight: 700; color: var(--brand); letter-spacing: .3px; margin-bottom: 9px; }
  .venture p { font-size: 14.8px; line-height: 25.5px; color: var(--ink); }
  .ground { top: 1304px; }
  .special { top: 1470px; }
  .started { left: 654px; top: 1567px; width: 142px; height: 48px; }

  /* founder */
  .founder-label { left: 152px; top: 1834px; font-size: 13.5px; font-weight: 600; color: var(--brand); }
  .founder-name { left: 151px; top: 1858px; font-size: 32px; font-weight: 600; color: var(--ink); letter-spacing: .5px; }
  .founder-bio { left: 152px; top: 1910px; font-size: 12.8px; line-height: 24.4px; color: var(--ink); white-space: nowrap; }
  .founder-bio p + p { margin-top: 7px; }
  .learn { left: 150px; top: 2177px; width: 142px; height: 48px; }
  .founder-frame { left: 611px; top: 1792px; width: 108px; height: 161px; background: var(--brand); }
  .founder-photo { left: 636px; top: 1814px; width: 393px; height: 466px; background: linear-gradient(180deg, #c9d3dc 0%, #9fa8b1 45%, #3a3c40 75%, #2b2c30 100%); }

  /* footer */
  .footer { left: 0; top: 2392px; width: 1200px; height: 210px; background: var(--brand); color: var(--white); }
  .contact-item { position: absolute; top: 48px; display: flex; gap: 18px; }
  .contact-icon { width: 41px; height: 41px; border: 1px solid rgba(255,255,255,.8); display: flex; align-items: center; justify-content: center; flex-shrink: 0; }
  .contact-item h4 { font-size: 14.5px; font-weight: 600; letter-spacing: .4px; margin-top: 2px; }
  .contact-item p { font-size: 14.5px; line-height: 20px; margin-top: 4px; }
  .contact-item .small { font-size: 13.5px; }
  .phone { left: 150px; }
  .address { left: 409px; }
  .email { left: 784px; }
  .footer-rule { position: absolute; left: 150px; top: 141px; width: 900px; height: 1px; background: rgba(255,255,255,.25); }
  .copyright { position: absolute; left: 0; width: 1200px; top: 163px; text-align: center; font-size: 13px; }
  .copyright b { font-weight: 600; }
</style>
</head>
<body>

<header>
  <div class="abs brand">
    <span class="brand-square"></span>
    <span class="brand-name">HALVERN<br>BUILDERS</span>
  </div>
  <a class="btn login" href="#">Investor Login</a>
</header>

<section class="hero">
  <div class="abs hero-band"></div>
  <div class="abs hero-photo" role="img" aria-label="Skyscrapers seen from below against a blue sky"></div>
  <h1 class="abs hero-title">HALVERN BUILDERS</h1>
  <p class="abs hero-text">Is An Entrepreneurial Firm Focused On<br>Building And Growing Transformational<br>Companies</p>
  <a class="btn contact" href="#">Contact Us Today</a>
</section>

<section class="mission">
  <h2 class="abs mission-title">OUR MISSION</h2>
  <div class="abs mission-photo" role="img" aria-label="Presenter showing charts on a flipchart to colleagues in an office"></div>
  <p class="abs mission-text">Mission Is To Build<br><b>Meaningful</b> Businesses<br>That Create <b>Enduring</b><br>Value By Impacting People<br>In A <b>Measurable</b> Way.</p>
</section>

<section class="ventures">
  <div class="abs venture-tab"></div>
  <div class="abs venture-band"></div>
  <div class="abs venture-photo" role="img" aria-label="Team reviewing documents and sticky notes on a wooden table"></div>
  <div class="abs venture ground">
    <h3>GROUND UP</h3>
    <p>Our ground up business applies a proven analytic process to identify value edge, a form of competitive advantage. We architect transformational companies and are deliberate in creating the foundation necessary to lead an industry.</p>
  </div>
  <div class="abs venture special">
    <h3>SPECIAL OPPORTUNITIES</h3>
    <p>We partner with exceptional teams that create value by<br>transforming lives. Our investment focus includes large<br>companies and spin-outs.</p>
  </div>
  <a class="btn started" href="#">Get Started</a>
</section>

<section class="founder">
  <p class="abs founder-label">HALVERN BUILDERS</p>
  <h2 class="abs founder-name">JHONE DOE</h2>
  <div class="abs founder-bio">
    <p>Lorem ipsum dolor sit amet, consectetuer adipiscing elitt,<br>sed diam nonummy nibh euismod tincidunt ut laoreet lotr<br>dolore magna aliquam erat volutpat. Ut wisi enim admiin<br>veniam, quis nostrud exercitation ullamcorper suscipit tell<br>lobortis nisl ut aliquip ex ea commodo consequat.</p>
    <p>Duis autem vel eum iriure dolor in hendrerit in vulputatiie<br>velit esse molestie consequat, vel illum dolore eu feugiat<br>nulla facilisis at vero eros et accumsan et iusto odio dign<br>issim qui blandit praesent luptatum zzril delenit augue tel<br>duis dolore te feugait nulla facilisi.</p>
  </div>
  <a class="btn learn" href="#">Learn More</a>
  <div class="abs founder-frame"></div>
  <div class="abs founder-photo" role="img" aria-label="Portrait of the founder in a dark suit with arms crossed"></div>
</section>

<footer class="abs footer">
  <div class="contact-item phone">
    <span class="contact-icon">
      <svg width="20" height="20" viewBox="0 0 24 24" fill="none" stroke="#fff" stroke-width="1.4" stroke-linejoin="round"><path d="M5 3h4l2 5-2.5 1.5a11 11 0 0 0 6 6L16 13l5 2v4a2 2 0 0 1-2 2A16 16 0 0 1 3 5a2 2 0 0 1 2-2z"/></svg>
    </span>
    <div><h4>PHONE</h4><p>123-456-7890</p></div>
  </div>
  <div class="contact-item address">
    <span class="contact-icon">
      <svg width="18" height="20" viewBox="0 0 24 24" fill="none" stroke="#fff" stroke-width="1.4"><path d="M12 22s7-7 7-12a7 7 0 0 0-14 0c0 5 7 12 7 12z"/><circle cx="12" cy="10" r="2.5"/></svg>
    </span>
    <div><h4>ADDRESS</h4><p class="small">123 Lorem ipsum dolor sit amet,<br>consectetuer adipiscing.</p></div>
  </div>
  <div class="contact-item email">
    <span class="contact-icon">
      <svg width="20" height="20" viewBox="0 0 24 24" fill="none" stroke="#fff" stroke-width="1.4" stroke-linejoin="round"><path d="M3 10l9-6 9 6v10H3z"/><path d="M3 10l9 6 9-6"/><path d="M7 8h10M8 11h8"/></svg>
    </span>
    <div><h4>EMAIL</h4><p>info@halvernbuilders.com</p></div>
  </div>
  <div class="footer-rule"></div>
  <p class="copyright">Copyright © 2021 <b>HALVERN BUILDERS.</b> All Rights Reserved.</p>
</footer>

</body>
</html>
```